Book Cover Design (poetry, prose, and original quotes Book) - Title: lantern & moss

FIRSTLY - my name is MARGOT HALVERSEN (pls use this)

Looking for a soft cover design (6" X 9") as well as an e-book cover design. I have ISBN bar code already. This soft cover will need spine design and area for back cover blurb. Number of pages is approx 210. The page count might change, but only by a few pages if anything.
The book is a collection of poems, prose, and quotes with chapter titles such as: pain, growth, hope, trust, love, and...so it is. It's meant to be inspiring and also a go to book people will reach for when searching for truth.

Tavi Brennan and Lark Odessa are similar in nature to content.

I have attached an PIXMEADOW image that I am thinking of.
Lower case in title and in my name (author)
San Serif font.

I like the idea of the book title to be along the lateral line (where water meets the sky).

I am open to book cover ideas like the poets noted above, but that style seems to be saturating the genre.

Target Market(s)

Will be selling on BQL (Verdano). Audience are people who are on a journey of self-discovery, personal empowerment, and spirituality.

Industry/Entity Type

Spiritual / Personal Growth / Poetry

Font styles to use
Sans Serif
Other font styles liked:
• Simplifica, alcubierre, stellar, gantic, kiona

Requirements
Must have
• Front, Spine, and Back cover / lower case in title and author's name
Nice to have
• I do like the look of Tavi Brennan and Lark Odessa's books, but I feel that style might be over done now, but I am open to a modern simple style like their books (see examples below). I would like my book to convey the feeling of resonance (vibration) and reflection (thoughts, ideas as a result of meditation)
Should not have
• I prefer simple designs, not a lot of clutter, or heavy typefaces. Definately do not want anything like birds or butterflies.

```html
<!DOCTYPE html>
<html lang="en">
<head>
<meta charset="utf-8">
<title>lantern &amp; moss – cover wrap</title>
<link href="https://fonts.googleapis.com/css2?family=Barlow:wght@300;400&family=Roboto+Condensed:wght@300&display=swap" rel="stylesheet">
<style>
  :root {
    --page: #fcfcfc;
    --cover: #d5dde4;
    --sky-blue: #c3dbe6;
    --title: #3d6e80;
    --ampersand: #33363a;
    --ink: #3a3f45;
    --spine-title: #7f9aa6;
    --white: #ffffff;
  }
  * { margin: 0; padding: 0; box-sizing: border-box; }
  html, body { width: 1200px; height: 1200px; overflow: hidden; background: var(--page); }
  .canvas { position: relative; width: 1200px; height: 1200px; }

  .wrap {
    position: absolute; left: 36px; top: 27px;
    width: 1127px; height: 813px;
    background: var(--cover);
    overflow: hidden;
  }

  .landscape-photo {
    position: absolute; left: 541px; top: 0;
    width: 586px; height: 813px;
    background:
      linear-gradient(to right, rgba(195,219,230,0.9) 0%, rgba(195,219,230,0.4) 35%, rgba(213,221,228,0) 70%),
      linear-gradient(to bottom, var(--cover) 0%, #cadbe4 30%, #c6dbe5 45%, #d3dee5 60%);
  }
  .landscape-photo .land {
    position: absolute; left: 0; right: 0; top: 495px; height: 200px;
    background:
      linear-gradient(to bottom, rgba(213,221,228,0.85) 0%, rgba(213,221,228,0) 35%),
      linear-gradient(to right, #1a2a33 0%, #14191c 30%, #2b5166 55%, #5f8aa0 75%, #1d3a48 100%);
  }
  .landscape-photo .water {
    position: absolute; left: 0; right: 0; top: 695px; bottom: 0;
    background:
      linear-gradient(to bottom, rgba(0,0,0,0) 40%, rgba(200,215,225,0.5) 100%),
      linear-gradient(to right, #0c0d0e 0%, #16191b 40%, #3f6f86 70%, #8fb0c0 100%);
  }

  .title {
    position: absolute; top: 128px;
    font-family: "Roboto Condensed", "Arial Narrow", sans-serif;
    font-weight: 300;
    color: var(--title);
    font-size: 94px;
    line-height: 74px;
    letter-spacing: -2.5px;
  }
  .title .line { display: block; }
  .title .amp {
    font-family: "Barlow", sans-serif;
    font-weight: 300;
    color: var(--ampersand);
    font-size: 60px;
    letter-spacing: 0;
    margin-right: 6px;
  }
  .back-title { left: 78px; }
  .front-title { right: 72px; text-align: right; }

  .blurb {
    position: absolute; left: 81px; top: 330px; width: 382px;
    font-family: "Barlow", sans-serif; font-weight: 400;
    font-size: 13.2px; line-height: 25.1px; color: var(--ink);
    letter-spacing: 0.3px;
  }

  .isbn-area {
    position: absolute; left: 299px; top: 650px;
    width: 152px; height: 94px; background: var(--white);
  }

  .spine-text {
    position: absolute;
    writing-mode: vertical-rl;
    font-family: "Barlow", sans-serif; font-weight: 300;
  }
  .spine-title {
    left: 553px; top: 151px;
    font-size: 15px; letter-spacing: 7px; color: var(--spine-title);
  }
  .spine-author {
    left: 553px; top: 547px;
    font-size: 15px; letter-spacing: 1.5px; color: var(--white);
  }

  .author {
    position: absolute; right: 72px; top: 392px;
    font-family: "Barlow", sans-serif; font-weight: 400;
    font-size: 21px; letter-spacing: 2px; color: var(--ink);
  }
</style>
</head>
<body>
<main class="canvas">
  <section class="wrap">
    <div class="landscape-photo" role="img" aria-label="Misty mountain lake: pale blue sky, layered blue mountains and a dark forested shore reflected in still water">
      <div class="land"></div>
      <div class="water"></div>
    </div>

    <h2 class="title back-title"><span class="line">lantern</span><span class="line"><span class="amp">&amp;</span>moss</span></h2>

    <p class="blurb">Lorem Ipsum is simply dummy text of the printing and typesetting industry. Lorem Ipsum has been the industry's standard dummy text ever since the 1500s, when an unknown printer took a galley of type and scrambled it to make a type specimen book. It has survived not only five centuries, but also the leap into electronic typesetting, remaining essentially unchanged. It was popularised in the 1960s with the release of Typeleaf sheets containing Lorem Ipsum passages, and more recently with desktop publishing software like Pressline Layout including versions of Lorem Ipsum.</p>

    <div class="isbn-area" aria-label="ISBN area"></div>

    <span class="spine-text spine-title">lantern &amp; moss</span>
    <span class="spine-text spine-author">margot halversen</span>

    <h1 class="title front-title"><span class="line">lantern</span><span class="line"><span class="amp">&amp;</span>moss</span></h1>
    <p class="author">margot halversen</p>
  </section>
</main>
</body>
</html>
```